Friends with Benefits 6 Bedroom Multi Share Student Accommodation Deal

We need a flyer design to put on our website to promote our 6 Bedroom Multishare rooms.Corvane Riverside; Student accommodation; 6 Bedroom Multi share Room; Find 5 friends to receive this deal. Deal includes Free Pizza Friday's; Weekly cleans; kitted out kitchen; free end of lease apartment clean; $1200 worth of value. We have attached what we came up with but we are not happy with the 'superhero' theme. We really need a tricky/clever tag line to grab the students attention.

Target Market(s)

University Students

Colors
ec1f27
ffffff

Requirements
Must have
• Corvane Riverside
• Student Accomodation
• Best Location in Brisbane!
• Friends with Benefits (unless you can come up with something better!)
• $1200 value
• 6 Bedroom Multi Share
• You find 5 friends and you are eligible for the deal!
Nice to have
• We came up with a superhero theme but not convinced it's right.
• We need some quirky grab lines to get the student's attention.
• check out our website
• https://www.corvane-example.com.au/corvane-riverside
Should not have
• Nothing - be imaginative! We want creativity, quirky and fun

```html
<!DOCTYPE html>
<html lang="en">
<head>
<meta charset="utf-8">
<title>Friends with Benefits – Corvane Riverside</title>
<link rel="stylesheet" href="https://fonts.googleapis.com/css2?family=Open+Sans:wght@600;700;800&family=Dancing+Script:wght@700&display=swap">
<style>
  :root {
    --brand-red: #ec1f27;
    --white: #ffffff;
    --wall-light: #f4f4f2;
    --wall-shade: #dcdcda;
    --ink: #3a3a3a;
    --script-orange: #f39a1e;
    --bubble-orange: #f2622e;
    --bubble-red: #e8202a;
    --bubble-peach: #f2b24f;
    --bubble-magenta: #d81c5f;
    --bubble-green: #8cc63f;
    --bubble-yellow: #f7cb2c;
  }
  * { margin: 0; padding: 0; box-sizing: border-box; }
  html, body { width: 898px; height: 1200px; overflow: hidden; background: var(--white); }
  .flyer {
    position: relative;
    width: 898px;
    height: 1200px;
    overflow: hidden;
    font-family: "Open Sans", Arial, sans-serif;
  }
  .wall-backdrop {
    position: absolute; inset: 0;
    background: radial-gradient(ellipse at 50% 45%, var(--wall-light) 0%, #ececea 60%, var(--wall-shade) 100%);
  }
  .headline {
    position: absolute;
    top: 42px; left: 0; width: 100%;
    text-align: center;
    color: var(--brand-red);
    font-weight: 800;
    font-size: 74px;
    line-height: 1;
    letter-spacing: 1px;
    white-space: nowrap;
  }
  .headline .connector {
    font-family: "Dancing Script", cursive;
    color: var(--script-orange);
    font-size: 52px;
    font-weight: 700;
    letter-spacing: 0;
    margin: 0 6px;
    position: relative;
    top: 6px;
  }
  .deal-condition {
    position: absolute;
    top: 136px; left: 0; width: 100%;
    text-align: center;
    color: var(--ink);
    font-weight: 600;
    font-size: 27px;
    letter-spacing: 0.5px;
    white-space: nowrap;
  }
  .student-photo {
    position: absolute;
    left: 400px; top: 400px;
    width: 480px; height: 719px;
    border-radius: 170px 170px 0 0;
    background: linear-gradient(180deg, #b88a5e 0%, #e6c383 26%, #f0d46e 40%, #6d8db6 60%, #4f729f 80%, #5b6f93 100%);
  }
  .bubbles { position: absolute; inset: 0; filter: drop-shadow(3px 5px 5px rgba(0,0,0,0.28)); }
  .bubble-label {
    position: absolute;
    transform: translate(-50%, -50%);
    color: var(--white);
    font-weight: 700;
    text-align: center;
    line-height: 1.25;
    font-size: 23px;
    white-space: nowrap;
  }
  .bubble-label.small { font-size: 18px; }
  .bubble-label.large { font-size: 30px; line-height: 1.2; }
  .location-tag {
    position: absolute;
    left: 47px; top: 1068px;
    font-family: "Dancing Script", cursive;
    font-weight: 700;
    font-size: 34px;
    color: #111;
    white-space: nowrap;
  }
  .name-band {
    position: absolute;
    left: 0; top: 1119px;
    width: 100%; height: 64px;
    background: var(--brand-red);
  }
  .name-band .residence-name {
    position: absolute;
    left: 47px; top: 50%;
    transform: translateY(-50%);
    color: var(--white);
    font-weight: 600;
    font-size: 32px;
  }
</style>
</head>
<body>
<main class="flyer">
  <div class="wall-backdrop" role="img" aria-label="White painted brick wall background"></div>

  <h1 class="headline">FRIENDS<span class="connector">with</span>BENEFITS</h1>
  <p class="deal-condition">- FIND 5 FRIENDS TO RECEIVE THIS DEAL -</p>

  <div class="student-photo" role="img" aria-label="Photo of a smiling student in a yellow top and jeans sitting cross-legged on a stack of books, looking up thoughtfully"></div>

  <svg class="bubbles" width="898" height="1200" viewBox="0 0 898 1200" aria-hidden="true">
    <g stroke="#ffffff" stroke-width="5" stroke-linejoin="round">
      <path fill="var(--bubble-orange)" d="M320 264 a124 78 0 1 1 210 56 L499 382 L470 338 a124 78 0 0 1 -150 -74 Z"/>
      <path fill="var(--bubble-red)" d="M647 302 a94 60 0 1 1 80 59 L693 388 L700 352 a94 60 0 0 1 -53 -50 Z"/>
      <path fill="var(--bubble-peach)" d="M134 416 a109 78 0 1 1 200 42 L361 494 L315 480 a109 78 0 0 1 -181 -64 Z"/>
      <path fill="var(--bubble-magenta)" d="M700 510 a83 71 0 1 1 40 60 L691 559 L712 540 a83 71 0 0 1 -12 -30 Z"/>
      <path fill="var(--bubble-green)" d="M90 670 a103 100 0 0 1 199 -36 L344 670 L286 712 a103 100 0 0 1 -196 -42 Z"/>
      <path fill="var(--bubble-yellow)" d="M110 919 a103 104 0 0 1 199 -40 L333 866 L314 940 a103 104 0 0 1 -204 -21 Z"/>
    </g>
  </svg>

  <div class="bubble-label" style="left:444px; top:264px;">KITTED OUT<br>KITCHEN</div>
  <div class="bubble-label" style="left:741px; top:302px; font-size:21px;">FREE PIZZA<br>FRIDAY'S</div>
  <div class="bubble-label" style="left:243px; top:416px;">WEEKLY<br>CLEANS</div>
  <div class="bubble-label small" style="left:783px; top:510px;">6 BEDROOM<br>MULTI SHARE</div>
  <div class="bubble-label" style="left:193px; top:670px; font-size:20px;">FREE END OF<br>LEASE APARTMENT<br>CLEAN</div>
  <div class="bubble-label large" style="left:213px; top:919px;">$1200<br>WORTH OF<br>VALUE</div>

  <p class="location-tag">Best Location in Brisbane!</p>

  <footer class="name-band">
    <span class="residence-name">Corvane Riverside</span>
  </footer>
</main>
</body>
</html>
```